Traineeway.Asia, a social enterprise in Asia, needs a website!

I need a website designed for Traineeway.Asia, which is a social enterprise in Asia that connects potential interns with internship opportunities in the region.

Please read the attached wireframe and submit a homepage designs with text, based on the attached wireframe, from which we will choose and select the best design. Please note that we only want website designs; functionality, coding and programming are not required

The designer that provides the best designed home page, will then design all other pages of the website, and will receive the fee. We have already come up with one design (see wireframe in the attached doc) that designers may review for ideas.

University and graduate students in Asia.

Social

5+ page

Sans Serif

• I want a website that doesn't require a significant amount of scrolling, and is well-designed so that it is easy to understand the website's purpose, how to navigate around the website, and utilize it.
• Easy to see all elements of the website without scrolling.

```html
<!DOCTYPE html>
<html lang="en">
<head>
<meta charset="utf-8">
<title>Traineeway.Asia – Home</title>
<link href="https://fonts.googleapis.com/css2?family=Montserrat:wght@400;500;600&family=Roboto:wght@400;500&display=swap" rel="stylesheet">
<style>
:root{
  --navy:#0d318a;
  --navy-dark:#0a2670;
  --sky:#1d9fd8;
  --green:#6cbd17;
  --green-dark:#4f9a0c;
  --ink:#222a36;
  --muted:#6b7280;
  --link:#1d3f9c;
  --panel:#e7ebf1;
  --rule:#cfd5de;
  --footer:#1d2029;
}
*{box-sizing:border-box;margin:0;padding:0}
html,body{width:775px;height:1200px;overflow:hidden;background:#fff}
body{font-family:'Roboto',sans-serif;color:var(--ink);font-size:7.5px;line-height:1.6}
.page{position:relative;width:775px;height:1200px}
.abs{position:absolute}
h2{font-family:'Montserrat',sans-serif;font-weight:500;font-size:14px;color:var(--ink)}
a{color:inherit;text-decoration:none}

/* header */
.header{left:0;top:0;width:775px;height:73px;background:linear-gradient(#fff,#eef0f3)}
.brand{left:72px;top:26px;display:flex;align-items:center;gap:6px;font-family:'Montserrat',sans-serif;font-weight:600;font-size:12px;color:var(--navy)}
.brand i{width:8px;height:8px;border-radius:50%;background:var(--green);display:block}
.nav{right:72px;top:31px;display:flex;gap:27px;font-family:'Montserrat',sans-serif;font-size:7px;font-weight:500;color:#2c3340}

/* hero */
.hero{left:0;top:73px;width:775px;height:294px;background:linear-gradient(90deg,#0c3189,#123d9e 50%,#0c3189)}
.slider{left:73px;top:20px;width:469px;height:253px;border:2px solid #fff;background:linear-gradient(135deg,#8a7d72,#d6c7b8 35%,#e9e4de 60%,#b9b3ad)}
.slider-caption{left:0;bottom:0;width:100%;height:55px;background:rgba(235,235,235,.78);padding:12px 18px;font-family:'Montserrat',sans-serif;font-size:10.5px;line-height:1.6;color:#333}
.dots{right:20px;bottom:20px;display:flex;gap:3px}
.dots span{width:7px;height:7px;border-radius:50%;background:#666}
.dots span.on{background:var(--green)}
.tweets{left:558px;top:20px;width:146px;height:255px;background:#fff}
.tweets-head{height:36px;background:var(--sky);color:#fff;font-family:'Montserrat',sans-serif;font-weight:500;font-size:9px;display:flex;align-items:center;padding-left:34px;position:relative}
.tweets-head::before{content:"";position:absolute;left:12px;top:12px;width:12px;height:12px;border-radius:50%;background:#fff}
.tweet{display:flex;gap:6px;margin:0 11px;padding:10px 0 6px;border-bottom:1px solid #ddd;height:69px}
.tweet-thumb{width:37px;height:30px;flex:none;background:linear-gradient(135deg,#2d6a8e,#86a6b5)}
.tweet-title{font-family:'Montserrat',sans-serif;font-size:7px;color:#222;line-height:1.4}
.tweet-text{font-size:6.5px;color:#666;line-height:1.6}
.tweet-link{font-size:6.5px;color:var(--sky)}
.tweet-more{font-size:5px;color:var(--navy)}

/* welcome */
.welcome{left:72px;top:395px;width:470px}
.welcome p{margin-top:9px;font-size:7px;line-height:2.4;color:#555}
.more{display:block;margin-top:6px;font-family:'Montserrat',sans-serif;font-weight:600;font-size:7px;color:var(--navy)}
.quote{left:558px;top:393px;width:146px;height:88px;background:var(--navy);color:#fff;text-align:center;font-family:'Montserrat',sans-serif;font-size:8.5px;line-height:2;padding-top:13px}
.btn-green{display:inline-block;background:var(--green);color:#1b3a00;font-family:'Montserrat',sans-serif;font-size:7px;font-weight:500;padding:5px 16px;margin-top:6px;border-radius:1px}

/* featured + team */
.panel{left:0;top:504px;width:775px;height:232px;background:var(--panel)}
.sec-head{display:flex;justify-content:space-between;align-items:center}
.btn-navy{background:var(--navy);color:#fff;font-family:'Montserrat',sans-serif;font-size:6.5px;font-weight:500;padding:5px 10px;border-radius:2px}
.featured{left:72px;top:21px;width:415px}
.jobs{display:grid;grid-template-columns:1fr 1fr;column-gap:18px;margin-top:12px}
.job{padding:0 0 7px;margin-bottom:9px}
.job:nth-child(-n+2){border-bottom:1px solid var(--rule)}
.job-date{font-family:'Montserrat',sans-serif;font-weight:500;font-size:7px;color:var(--link)}
.job-title{font-family:'Montserrat',sans-serif;font-size:7.5px;line-height:1.75;color:#222;margin-top:3px}
.job-text{font-size:7px;color:#666;line-height:1.8;margin-top:2px}
.team{left:503px;top:21px;width:201px}
.member{display:flex;gap:7px;margin-top:11px}
.member:first-of-type{margin-top:14px}
.avatar{width:45px;height:44px;flex:none;background:linear-gradient(#c9d1da,#6b7380)}
.m-name{font-family:'Montserrat',sans-serif;font-size:7.5px;color:var(--link)}
.m-role{font-family:'Montserrat',sans-serif;font-size:7.5px;color:#222;line-height:1.4}
.m-bio{font-size:6.5px;color:#777;line-height:1.85}

/* resources */
.resources{left:72px;top:760px;width:470px}
.res{display:flex;gap:10px;margin-top:11px;height:83px}
.res:first-of-type{margin-top:12px}
.res-img{width:121px;height:77px;flex:none}
.res-body{flex:1}
.res-title{font-family:'Montserrat',sans-serif;font-size:8.5px;line-height:1.6;color:#222;height:26px}
.res-meta{display:flex;justify-content:space-between;font-size:7px;color:#777;padding:3px 0 4px;border-bottom:1px solid var(--rule)}
.res-meta b{font-weight:400;color:var(--link)}
.icons{display:flex;gap:6px;align-items:center;color:#555}
.icons i{width:7px;height:6px;border:1.2px solid var(--green);display:block;border-radius:1px}
.res-text{font-size:7px;color:#666;line-height:2;margin-top:6px}
.side{left:557px;top:760px;width:147px}
.side p{font-size:7px;color:#666;line-height:2.4;margin-top:6px}
.btn-block{display:block;height:34px;background:var(--navy);color:#fff;text-align:center;line-height:34px;font-family:'Montserrat',sans-serif;font-size:9.5px;font-weight:500;border-radius:2px;margin-top:10px}
.side h2+.newsletter{margin-top:0}
.email{height:28px;border:1px solid var(--rule);margin-top:6px;font-size:6.5px;color:#aaa;padding:8px 10px}

/* CTA */
.cta{left:0;top:1076px;width:775px;height:74px;background:linear-gradient(var(--navy),var(--navy-dark))}
.cta p{position:absolute;left:98px;top:16px;color:#fff;font-size:12.5px;line-height:1.65;width:440px}
.cta a{position:absolute;left:547px;top:22px;width:131px;height:31px;background:var(--green);color:#1b3a00;font-family:'Montserrat',sans-serif;font-size:8px;font-weight:500;text-align:center;line-height:31px;border-radius:2px}

/* footer */
.footer{left:0;top:1150px;width:775px;height:50px;background:var(--footer);color:#b8bcc6;font-size:7px}
.footer .copy{position:absolute;left:71px;top:21px}
.footer .social{position:absolute;left:371px;top:18px;display:flex;gap:3px}
.footer .social span{width:15px;height:15px;border-radius:50%;background:#9fb4cc}
.footer .links{position:absolute;right:71px;top:21px}
</style>
</head>
<body>
<div class="page">

  <header class="header abs">
    <a class="brand abs" href="#"><i></i>Traineeway.Asia</a>
    <nav class="nav abs">
      <a href="#">About Us</a><a href="#">Search Internships</a><a href="#">Post an Internship</a><a href="#">Login</a><a href="#">Registration</a>
    </nav>
  </header>

  <section class="hero abs">
    <div class="slider abs" role="img" aria-label="Photo of students sitting attentively in a lecture room">
      <div class="slider-caption abs">Want to get professional experience while still in<br>college/university or graduate school?</div>
      <div class="dots abs"><span></span><span class="on"></span><span></span><span></span></div>
    </div>
    <aside class="tweets abs">
      <div class="tweets-head">Latest Tweets</div>
      <div class="tweet">
        <div class="tweet-thumb" role="img" aria-label="Thumbnail of a person at a chalkboard"></div>
        <div><div class="tweet-title">Lorem ipsum dolor sit</div><div class="tweet-text">Ut wisi enim ad minim veniam, quis...</div><div class="tweet-link">www.samplelink.com/item</div><div class="tweet-more">▯ View summary</div></div>
      </div>
      <div class="tweet">
        <div class="tweet-thumb" role="img" aria-label="Thumbnail of a graduation cap" style="background:linear-gradient(135deg,#3a2b22,#c79a6b)"></div>
        <div><div class="tweet-title">Duis autem vel eum</div><div class="tweet-text">Lorem ipsum dolor sit amet...</div><div class="tweet-link">www.samplelink.com/item</div><div class="tweet-more">▯ View summary</div></div>
      </div>
      <div class="tweet">
        <div class="tweet-thumb" role="img" aria-label="Thumbnail of a person at a chalkboard"></div>
        <div><div class="tweet-title">Claritas est etiam</div><div class="tweet-text">Ut wisi enim ad minim veniam, quis...</div><div class="tweet-link">www.samplelink.com/item</div><div class="tweet-more">▯ View summary</div></div>
      </div>
    </aside>
  </section>

  <section class="welcome abs">
    <h2>Welcome To Traineeway.Asia</h2>
    <p>Traineeway.Asia is a no-cost, workable, and efficient platform for companies to advertise internship opportunities and for students / potential interns to identify internship opportunities throughout Asia. Particularly with the rising of the ASEAN Economic Community, students in the region must get international work experience to be competitive.</p>
    <a class="more" href="#">READ MORE</a>
  </section>
  <div class="quote abs">“IF YOU ARE SEEKING AN<br>INTERNSHIP OPPORTUNITY”<br><a class="btn-green" href="#">CLICK HERE</a></div>

  <section class="panel abs">
    <div class="featured abs">
      <div class="sec-head"><h2>Featured Internships</h2><a class="btn-navy" href="#">VIEW ALL</a></div>
      <div class="jobs">
        <div class="job"><div class="job-date">13 APR, 2015</div><div class="job-title">Ut wisi enim ad minim veniam, quis nostrud exerci tation ullamcorper suscipit lobortis</div><div class="job-text">Lorem ipsum dolor sit amet, consectetuer adipiscing elit, sed diam nonummy nibh...</div></div>
        <div class="job"><div class="job-date">13 APR, 2015</div><div class="job-title">Duis autem vel eum iriure dolor in hendrerit in vulputate velit esse molestie consequat</div><div class="job-text">Lorem ipsum dolor sit amet, consectetuer adipiscing elit, sed diam nonummy nibh...</div></div>
        <div class="job"><div class="job-date">13 APR, 2015</div><div class="job-title">Typi non habent claritatem insitam; est usus legentis in iis qui</div><div class="job-text">Lorem ipsum dolor sit amet, consectetuer adipiscing elit, sed diam nonummy nibh...</div></div>
        <div class="job"><div class="job-date">13 APR, 2015</div><div class="job-title">Mirum est notare quam littera gothica, quam nunc putamus parum</div><div class="job-text">Lorem ipsum dolor sit amet, consectetuer adipiscing elit, sed diam nonummy nibh...</div></div>
      </div>
    </div>
    <div class="team abs">
      <div class="sec-head"><h2>Our Team</h2><a class="btn-navy" href="#">VIEW ALL</a></div>
      <div class="member"><div class="avatar" role="img" aria-label="Portrait of the founder"></div><div><div class="m-name">Maren Holloway</div><div class="m-role">Founder</div><div class="m-bio">Maren volunteers his time to Traineeway.Asia, and is managing director of Kestrel...</div></div></div>
      <div class="member"><div class="avatar" role="img" aria-label="Portrait of the chief operating officer"></div><div><div class="m-name">Linh Vo</div><div class="m-role">Chief Operating Officer (COO)</div><div class="m-bio">Linh volunteers her time at Traineeway.Asia and is its Chief Operating Officer...</div></div></div>
      <div class="member"><div class="avatar" role="img" aria-label="Portrait of the website designer"></div><div><div class="m-name">Tuan Pham</div><div class="m-role">Initial Website Design</div><div class="m-bio">At Traineeway.Asia, Tuan developed the initial layout for the website and provided...</div></div></div>
    </div>
  </section>

  <section class="resources abs">
    <h2>Resources</h2>
    <article class="res">
      <div class="res-img" role="img" aria-label="Photo of an audience at a seminar" style="background:linear-gradient(#9fb0c4,#4a4f58)"></div>
      <div class="res-body"><div class="res-title">Lorem ipsum dolor sit amet, consectetuer adipiscing elit, sed diam nonummy nibh</div><div class="res-meta"><span>By <b>Sam Reed</b> &nbsp; Apr 12, 2015</span><span class="icons"><i></i><i></i><i></i>12</span></div><div class="res-text">Ut wisi enim ad minim veniam, quis nostrud exerci tation ullamcorper suscipit lobortis nisl ut aliquip ex ea commodo consequat.</div></div>
    </article>
    <article class="res">
      <div class="res-img" role="img" aria-label="Photo of a team working around a wooden table" style="background:linear-gradient(#6b4a33,#9a7456)"></div>
      <div class="res-body"><div class="res-title">Duis autem vel eum iriure dolor in hendrerit in vulputate velit esse molestie consequat</div><div class="res-meta"><span>By <b>Sam Reed</b> &nbsp; Apr 12, 2015</span><span class="icons"><i></i><i></i><i></i>12</span></div><div class="res-text">Ut wisi enim ad minim veniam, quis nostrud exerci tation ullamcorper suscipit lobortis nisl ut aliquip ex ea commodo consequat.</div></div>
    </article>
    <article class="res">
      <div class="res-img" role="img" aria-label="Photo of young professionals against a city skyline" style="background:linear-gradient(#a9cbe8,#e4ecf2 60%,#8d8f8a)"></div>
      <div class="res-body"><div class="res-title">Eodem modo typi, qui nunc nobis videntur parum clari, fiant sollemnes in futurum</div><div class="res-meta"><span>By <b>Sam Reed</b> &nbsp; Apr 12, 2015</span><span class="icons"><i></i><i></i><i></i>12</span></div><div class="res-text">Ut wisi enim ad minim veniam, quis nostrud exerci tation ullamcorper suscipit lobortis nisl ut aliquip ex ea commodo consequat.</div></div>
    </article>
  </section>

  <aside class="side abs">
    <h2>Post an Internship</h2>
    <p>Quis nostrud exerci tation ullamcorper suscipit lobortis nisl ut aliquip ex ea commodo consequat.</p>
    <a class="btn-block" href="#">CLICK HERE</a>
    <h2 style="margin-top:20px">Newsletter Signup</h2>
    <p>Lorem ipsum dolor sit amet, consectetuer adipiscing elit, sed diam.</p>
    <div class="email">Email Address</div>
    <a class="btn-block" href="#" style="margin-top:13px">SUBSCRIBE NOW</a>
  </aside>

  <section class="cta abs">
    <p>Want to offer an internship opportunity to an undergraduate or graduate student in Asia?</p>
    <a href="#">REGISTER NOW ➜</a>
  </section>

  <footer class="footer abs">
    <span class="copy">@ Traineeway.Asia. All Right Reserved.</span>
    <div class="social"><span></span><span></span></div>
    <span class="links">Terms and Conditions &nbsp;|&nbsp; Contact Us</span>
  </footer>

</div>
</body>
</html>
```